Beneath a Quiet Lantern (CD cover)

A CD cover that incorporates (if possible) a photo (or photos) with original art. (I'm flexible on this) Should have a sense of mystery... pensive, but also suggest expansiveness.

I'm open to putting photo on front of CD and art on back or inside, or vice versa, as I don't think they can be incorporated effectively??

I need a design primarily for the front, but possibly the back too (in other words, the sections that will be most visible prior to opening the CD.) This will be a "sleeve" or wallet style CD cover with 4 panels.

I'm including the liner notes, list of songs, artists, etc, but it's not necessary to lay that out too as that will be in the inside panels.

Target Market(s)

Jazz and independent/original music listeners

Industry/Entity Type

Artists

Requirements
Must have
• Cover:
Title of CD
My name
Names of band members
Photo or Art

Back or Inside:
Song titles
Photos of band and recording session
Introductory/explanatory verbiage
Nice to have
• Original art
Should not have
• No need to incorporate the liner notes attached - this was provided simply to give more information to designers - to give them more of a feel of what the album is about.

```html
<!DOCTYPE html>
<html lang="en">
<head>
<meta charset="utf-8">
<title>Beneath a Quiet Lantern – CD Cover</title>
<link rel="stylesheet" href="https://fonts.googleapis.com/css2?family=Anton&family=Norican&display=swap">
<style>
  :root {
    --page: #ffffff;
    --ink-dark: #3b0f0b;
    --paint-deep: #5a1a0c;
    --paint-rust: #9a3d12;
    --paint-amber: #d98a1c;
    --paint-gold: #f2c21e;
    --paint-light: #fbf4d6;
    --name-tint: rgba(246, 190, 42, 0.62);
    --label: #222222;
  }
  * { margin: 0; padding: 0; box-sizing: border-box; }
  html, body {
    width: 1200px;
    height: 1181px;
    overflow: hidden;
    background: var(--page);
  }
  .sheet {
    position: relative;
    width: 1200px;
    height: 1181px;
  }
  .cover {
    position: absolute;
    left: 115px;
    top: 57px;
    width: 971px;
    height: 964px;
    overflow: hidden;
  }
  .cover-art {
    position: absolute;
    inset: 0;
    background:
      linear-gradient(180deg, transparent 0%, transparent 90%, rgba(60,20,8,0.75) 93%, #2a0d06 100%),
      radial-gradient(ellipse 55% 30% at 8% 68%, var(--paint-light) 0%, rgba(251,244,214,0.6) 35%, transparent 75%),
      radial-gradient(ellipse 70% 40% at 30% 75%, var(--paint-gold) 0%, rgba(242,194,30,0.5) 50%, transparent 85%),
      linear-gradient(200deg, var(--paint-deep) 0%, var(--paint-rust) 30%, var(--paint-amber) 55%, var(--paint-gold) 78%, var(--paint-amber) 100%);
  }
  .artist-name {
    position: absolute;
    left: 30px;
    top: -40px;
    font-family: 'Anton', sans-serif;
    font-size: 338px;
    line-height: 262px;
    color: var(--name-tint);
    text-transform: uppercase;
    white-space: nowrap;
    letter-spacing: 2px;
  }
  .artist-name span { display: block; }
  .album-title {
    position: absolute;
    left: 0;
    right: 0;
    top: 600px;
    text-align: center;
    font-family: 'Norican', cursive;
    font-size: 80px;
    color: var(--ink-dark);
    white-space: nowrap;
  }
  .credits {
    position: absolute;
    left: 0;
    right: 0;
    top: 734px;
    text-align: center;
    font-family: 'Norican', cursive;
    color: var(--ink-dark);
  }
  .credits .with { font-size: 30px; line-height: 44px; }
  .credits .players { font-size: 34px; line-height: 50px; white-space: nowrap; }
  .credits .sep { padding: 0 10px; font-family: Arial, sans-serif; font-size: 28px; }
  .panel-label {
    position: absolute;
    left: 0;
    right: 0;
    top: 1090px;
    text-align: center;
    font-family: Arial, Helvetica, sans-serif;
    font-size: 22px;
    color: var(--label);
  }
</style>
</head>
<body>
<main class="sheet">
  <section class="cover">
    <div class="cover-art" role="img" aria-label="Abstract painting in brushed amber, gold and rust tones with a bright horizon glow and a dark band at the bottom"></div>
    <h1 class="artist-name"><span>Calla</span><span>Winsloe</span></h1>
    <h2 class="album-title">Beneath a Quiet Lantern</h2>
    <div class="credits">
      <p class="with">with</p>
      <p class="players">Owen Falkridge<span class="sep">|</span>Tobias Renner<span class="sep">|</span>Hal Dormund</p>
      <p class="players">Ray Siddons<span class="sep">|</span>Eli Marsh<span class="sep">|</span>Nils Tovar<span class="sep">|</span>Ward Pellham</p>
    </div>
  </section>
  <p class="panel-label">FRONT COVER</p>
</main>
</body>
</html>
```